Financial Services Company power point theme design

We need a PowerPoint theme designed for client presentations and company orientations. We do like modern designs using blue colors. attached is our logos the logo colors may change as needed to fit the theme. Landscape 16: 9 is acceptable

Industry/Entity Type

Financial Service

Colors

Designer to choose colors to be used in the design.

```html
<!DOCTYPE html>
<html lang="en">
<head>
<meta charset="utf-8">
<title>Keystone Ledger Group — Presentation Theme</title>
<link href="https://fonts.googleapis.com/css2?family=Roboto:wght@300;400;500;700&display=swap" rel="stylesheet">
<style>
:root{
  --navy:#1f3768;
  --navy-deep:#172d57;
  --blue:#2a7fc1;
  --blue-soft:#8fa3c8;
  --pale:#c9d2e4;
  --ice:#dbe6f2;
  --ink:#333;
  --muted:#777;
  --stage:#a7a7a9;
  --orange:#e8792b;
  --yellow:#f2b41c;
  --gray:#a3a3a3;
  --box:#d6d6d6;
}
*{box-sizing:border-box;margin:0;padding:0}
html,body{width:1200px;height:1200px;overflow:hidden;background:var(--stage);font-family:"Roboto",Arial,sans-serif;color:var(--ink)}
.board{position:relative;width:1200px;height:1200px}
.slide{position:absolute;width:361px;height:270px;background:#fff;overflow:hidden;box-shadow:0 1px 3px rgba(0,0,0,.25)}
.slide.dark{background:var(--navy)}
.c1{left:32px}.c2{left:417px}.c3{left:804px}
.r1{top:26px}.r2{top:316px}.r3{top:613px}.r4{top:910px}
.abs{position:absolute}
.side-art{position:absolute;left:0;top:0;width:128px;height:270px}
.side-art.on-navy{background:linear-gradient(160deg,rgba(255,255,255,.09),rgba(255,255,255,.03) 70%,rgba(255,255,255,0))}
.side-art.on-white{background:linear-gradient(160deg,var(--blue) 0%,var(--blue-soft) 45%,var(--navy) 100%)}
.side-art.on-white-soft{background:linear-gradient(160deg,var(--ice),#e6ebf1 55%,var(--pale))}
.brand{font-weight:400;letter-spacing:.5px;line-height:1.1}
.cover-brand{position:absolute;right:32px;top:40px;color:#fff;font-size:12px;text-align:left}
.cover-brand.onwhite{color:var(--navy);top:66px;right:34px;text-align:center}
.headline{position:absolute;right:24px;top:183px;font-weight:300;font-size:18px;line-height:1.3;text-align:right;color:#fff;letter-spacing:-.2px}
.headline.ink{color:var(--navy)}
.subline{position:absolute;right:24px;top:234px;font-size:6.5px;font-weight:400;color:#fff;letter-spacing:.2px}
.subline.ink{color:var(--navy)}
.title{position:absolute;left:0;right:0;top:18px;text-align:center;font-size:12.5px;font-weight:400;color:#111;letter-spacing:.2px}
.rule{position:absolute;left:20px;right:20px;top:34px;height:1px;background:var(--navy)}
.lede{position:absolute;left:20px;right:20px;top:40px;text-align:center;font-size:8.5px;color:var(--navy)}
.body{font-size:4.3px;line-height:1.5;color:var(--muted)}
.footer{position:absolute;left:0;right:0;bottom:7px;height:9px}
.footer .bar{position:absolute;left:0;top:0;width:236px;height:9px;background:var(--navy);clip-path:polygon(0 0,100% 0,97% 100%,0 100%)}
.footer .tab{position:absolute;right:0;top:0;width:46px;height:9px;background:var(--blue);clip-path:polygon(5% 0,100% 0,100% 100%,0 100%);color:#fff;font-size:5px;text-align:right;padding-right:10px;line-height:9px}
.footer .mark{position:absolute;left:244px;top:-2px;font-size:4.6px;color:var(--navy);width:70px;text-align:center;line-height:1.1}
.toc-item{position:absolute;width:105px;height:20px}
.toc-num{position:absolute;left:0;top:3px;width:14px;height:14px;border-radius:50%;background:#555;color:#fff;font-size:4.5px;text-align:center;line-height:14px}
.toc-text{position:absolute;left:20px;top:0;border-left:1px solid var(--navy);padding-left:3px}
.toc-text b{display:block;font-weight:400;font-size:7px;color:var(--navy)}
.toc-text span{display:block;font-size:3.6px;color:var(--muted);line-height:1.3}
.budget{position:absolute;left:21px;top:84px;width:320px;border-collapse:collapse;font-size:4.3px;color:#555}
.budget th{background:var(--navy);color:#fff;font-weight:400;text-align:left;padding:0 5px;height:13px}
.budget td{height:13.5px;padding:0 5px;border-bottom:1px solid #fff}
.budget tr.alt td{background:var(--pale)}
.budget td.num{width:22px;text-align:left;color:#333}
.svc{position:absolute;top:84px;width:80px;text-align:center}
.svc svg{display:block;margin:0 auto 8px}
.card{position:absolute;top:114px;width:83px;height:124px;background:var(--box);padding:4px}
.card h4{font-weight:400;font-size:5.5px;color:var(--blue);line-height:1.2;margin-bottom:4px}
.photo-circle{position:absolute;top:49px;width:62px;height:62px;border-radius:50%;border:1.5px solid #5a9b3f}
.photo{position:absolute}
.bullets{position:absolute;left:230px;top:78px;width:114px;list-style:none}
.bullets li{position:relative;padding-left:9px;margin-bottom:6px;font-size:4.3px;line-height:1.5;color:#444;text-align:justify}
.bullets li::before{content:"";position:absolute;left:0;top:1px;width:0;height:0;border-left:3px solid transparent;border-right:3px solid transparent;border-bottom:5px solid var(--navy)}
.contact{position:absolute;top:228px;left:78px;display:flex;gap:10px;font-size:4.6px;line-height:1.6}
.contact div{border-left:1px solid currentColor;padding-left:4px}
.contact .brand{border:0;padding:0;font-size:5.5px;align-self:center}
.dark .contact{color:#fff}
.light .contact{color:var(--navy)}
</style>
</head>
<body>
<main class="board">

<section class="slide dark c1 r1">
  <div class="side-art on-navy" role="img" aria-label="Faint decorative geometric panel"></div>
  <div class="cover-brand brand">KEYSTONE<br>LEDGER GROUP</div>
  <h1 class="headline">YOUR HEADLINE TEXT<br>HERE TO PUT</h1>
  <p class="subline">LOREM IPSUM IS SIMPLY DUMMY HAS BEEN</p>
</section>

<section class="slide c2 r1">
  <div class="side-art on-white" role="img" aria-label="Decorative geometric panel in blue tones"></div>
  <div class="cover-brand brand onwhite">KEYSTONE<br>LEDGER GROUP</div>
  <h1 class="headline ink">YOUR HEADLINE TEXT<br>HERE TO PUT</h1>
  <p class="subline ink">LOREM IPSUM IS SIMPLY DUMMY HAS BEEN</p>
</section>

<section class="slide c3 r1">
  <h2 class="title">TABLE OF CONTENT</h2>
  <div class="rule"></div>
  <div class="toc-item" style="left:20px;top:58px"><span class="toc-num">1</span><div class="toc-text"><b>About Us</b><span>Lorem Ipsum is simply dummy<br>text of the printing and typeset</span></div></div>
  <div class="toc-item" style="left:141px;top:58px"><span class="toc-num">2</span><div class="toc-text"><b>Who We Are</b><span>Lorem Ipsum is simply dummy<br>text of the printing and typeset</span></div></div>
  <div class="toc-item" style="left:256px;top:58px"><span class="toc-num">3</span><div class="toc-text"><b>What We Do</b><span>Lorem Ipsum is simply dummy<br>text of the printing and typeset</span></div></div>
  <div class="toc-item" style="left:20px;top:104px"><span class="toc-num">4</span><div class="toc-text"><b>About Us</b><span>Lorem Ipsum is simply dummy<br>text of the printing and typeset</span></div></div>
  <div class="toc-item" style="left:141px;top:104px"><span class="toc-num">5</span><div class="toc-text"><b>About Us</b><span>Lorem Ipsum is simply dummy<br>text of the printing and typeset</span></div></div>
  <div class="toc-item" style="left:256px;top:104px"><span class="toc-num">6</span><div class="toc-text"><b>About Us</b><span>Lorem Ipsum is simply dummy<br>text of the printing and typeset</span></div></div>
  <div class="toc-item" style="left:20px;top:150px"><span class="toc-num">7</span><div class="toc-text"><b>About Us</b><span>Lorem Ipsum is simply dummy<br>text of the printing and typeset</span></div></div>
  <div class="toc-item" style="left:141px;top:150px"><span class="toc-num">8</span><div class="toc-text"><b>About Us</b><span>Lorem Ipsum is simply dummy<br>text of the printing and typeset</span></div></div>
  <div class="toc-item" style="left:256px;top:150px"><span class="toc-num">9</span><div class="toc-text"><b>About Us</b><span>Lorem Ipsum is simply dummy<br>text of the printing and typeset</span></div></div>
  <div class="toc-item" style="left:20px;top:195px"><span class="toc-num">7</span><div class="toc-text"><b>About Us</b><span>Lorem Ipsum is simply dummy<br>text of the printing and typeset</span></div></div>
  <div class="toc-item" style="left:141px;top:195px"><span class="toc-num">8</span><div class="toc-text"><b>About Us</b><span>Lorem Ipsum is simply dummy<br>text of the printing and typeset</span></div></div>
  <div class="toc-item" style="left:256px;top:195px"><span class="toc-num">9</span><div class="toc-text"><b>About Us</b><span>Lorem Ipsum is simply dummy<br>text of the printing and typeset</span></div></div>
  <footer class="footer"><span class="bar"></span><span class="mark brand">KEYSTONE<br>LEDGER GROUP</span><span class="tab">1</span></footer>
</section>

<section class="slide c1 r2">
  <h2 class="title">BUDGET PLAN</h2>
  <p class="abs" style="left:21px;top:40px;font-size:7px;font-weight:700;color:#111">Lorem ipsum dolor sit amet, consectetur adipisicing elit, sed do eiusmod tempor incid-</p>
  <div class="rule" style="top:49px;left:21px"></div>
  <p class="abs body" style="left:21px;right:20px;top:51px">Lorem Ipsum is simply dummy text of the printing and typesetting industry. Lorem Ipsum has been the industry's standard dummy text ever since the 1500s, when an unknown printer took a galley of type and scrambled it to make a type specimen book. It has survived not only five centuries, but also the leap into electronic typesetting, remaining essentially unchanged.</p>
  <table class="budget">
    <tr><th></th><th>Lorem ipsum is simply dummy text of</th><th>Lorem ipsum is simply</th><th>Lorem Ipsum</th><th>Lorem Ipsum</th></tr>
    <tr><td class="num">1</td><td>Lorem Ipsum is simply dummy</td><td>Lorem Ipsum is simply</td><td>109</td><td>2190</td></tr>
    <tr class="alt"><td class="num">2</td><td>Lorem Ipsum is simply</td><td>Lorem Ipsum is simply</td><td>109</td><td>2190</td></tr>
    <tr><td class="num">3</td><td>Lorem Ipsum is simply dummy text</td><td>Lorem Ipsum is simply</td><td>109</td><td>2190</td></tr>
    <tr class="alt"><td class="num">4</td><td>Lorem Ipsum is simply dummy text</td><td>Lorem Ipsum is simply</td><td>109</td><td>2190</td></tr>
    <tr><td class="num">5</td><td>Lorem Ipsum is</td><td>Lorem Ipsum is simply</td><td>109</td><td>2190</td></tr>
    <tr class="alt"><td class="num">0</td><td>Lorem Ipsum is simply</td><td>Lorem Ipsum is simply</td><td>109</td><td>2190</td></tr>
    <tr><td class="num">0</td><td>Lorem Ipsum is simply dummy</td><td>Lorem Ipsum is simply</td><td>109</td><td>2190</td></tr>
    <tr class="alt"><td class="num">0</td><td>Lorem Ipsum is simply dummy text</td><td>Lorem Ipsum is simply</td><td>109</td><td>2190</td></tr>
    <tr><td class="num">0</td><td>Lorem Ipsum is simply dummy text</td><td>Lorem Ipsum is simply</td><td>109</td><td>2190</td></tr>
    <tr class="alt"><td class="num">0</td><td>Lorem Ipsum is</td><td>Lorem Ipsum is simply</td><td>109</td><td>2190</td></tr>
    <tr><td class="num">0</td><td>Lorem Ipsum is simply</td><td>Lorem Ipsum is simply</td><td>109</td><td>2190</td></tr>
  </table>
  <footer class="footer"><span class="bar"></span><span class="mark brand">KEYSTONE<br>LEDGER GROUP</span><span class="tab">3</span></footer>
</section>

<section class="slide c2 r2">
  <h2 class="title">OUR SERVICES</h2>
  <div class="rule"></div>
  <p class="lede" style="top:41px">Lorem ipsum dolor sit amet, consectetuer adipiscing elit, sed diam</p>
  <div class="svc" style="left:22px">
    <svg width="48" height="48" viewBox="0 0 48 48"><circle cx="24" cy="24" r="22" fill="#fff" stroke="var(--navy)" stroke-width="2"/><circle cx="24" cy="24" r="19" fill="#6b6b6b"/><path d="M13 25l6-6 5 3 5-3 6 6-6 6-5-3-5 3z" fill="none" stroke="#fff" stroke-width="2" stroke-linejoin="round"/></svg>
    <p class="body">Lorem Ipsum is simply dummy text of the printing and typesetting industry. Lorem Ipsum has been Lorem Ipsum is simply dummy text of the printing and typesetting industry. Lorem Ipsum</p>
  </div>
  <div class="svc" style="left:107px">
    <svg width="48" height="48" viewBox="0 0 48 48"><circle cx="24" cy="24" r="22" fill="#fff" stroke="var(--navy)" stroke-width="2"/><circle cx="24" cy="24" r="19" fill="#6b6b6b"/><path d="M14 27v-4a10 10 0 0 1 20 0v4" fill="none" stroke="#fff" stroke-width="2"/><rect x="12" y="25" width="5" height="8" rx="2" fill="#fff"/><rect x="31" y="25" width="5" height="8" rx="2" fill="#fff"/></svg>
    <p class="body">Lorem Ipsum is simply dummy text of the printing and typesetting industry. Lorem Ipsum has been Lorem Ipsum is simply dummy text of the printing and typesetting industry. Lorem Ipsum</p>
  </div>
  <div class="svc" style="left:192px">
    <svg width="48" height="48" viewBox="0 0 48 48"><circle cx="24" cy="24" r="22" fill="#fff" stroke="var(--navy)" stroke-width="2"/><circle cx="24" cy="24" r="19" fill="#6b6b6b"/><rect x="16" y="13" width="16" height="22" rx="1" fill="none" stroke="#fff" stroke-width="2"/><path d="M19 20h10M19 25h10M19 30h6" stroke="#fff" stroke-width="1.6"/></svg>
    <p class="body">Lorem Ipsum is simply dummy text of the printing and typesetting industry. Lorem Ipsum has been Lorem Ipsum is simply dummy text of the printing and typesetting industry. Lorem Ipsum</p>
  </div>
  <div class="svc" style="left:277px">
    <svg width="48" height="48" viewBox="0 0 48 48"><circle cx="24" cy="24" r="22" fill="#fff" stroke="var(--navy)" stroke-width="2"/><circle cx="24" cy="24" r="19" fill="#6b6b6b"/><rect x="15" y="26" width="4" height="8" fill="#fff"/><rect x="22" y="22" width="4" height="12" fill="#fff"/><rect x="29" y="18" width="4" height="16" fill="#fff"/><path d="M14 22l8-6 5 3 7-6" fill="none" stroke="#fff" stroke-width="1.6"/></svg>
    <p class="body">Lorem Ipsum is simply dummy text of the printing and typesetting industry. Lorem Ipsum has been Lorem Ipsum is simply dummy text of the printing and typesetting industry. Lorem Ipsum</p>
  </div>
  <footer class="footer"><span class="bar"></span><span class="mark brand">KEYSTONE<br>LEDGER GROUP</span><span class="tab">3</span></footer>
</section>

<section class="slide c3 r2">
  <h2 class="title">YOUR HEADLINE HERE TO PUT</h2>
  <div class="rule"></div>
  <p class="lede" style="top:41px">Lorem ipsum dolor sit amet, consectetur adipisicing do eiusmod</p>
  <p class="abs" style="left:20px;width:150px;top:79px;text-align:center;font-size:7.5px;color:#111;line-height:1.25">USE OF FOUNDER SEED CAPITAL<br>$1.12M SINCE JAN 2014</p>
  <p class="abs" style="left:60px;top:103px;font-size:3.8px;color:#444">
    <span style="color:var(--blue)">■</span> marketing &nbsp;<span style="color:var(--orange)">■</span> sg&amp;a &nbsp;<span style="color:var(--gray)">■</span> r&amp;d &nbsp;<span style="color:var(--yellow)">■</span> 1x legal</p>
  <svg class="abs" style="left:45px;top:117px" width="110" height="110" viewBox="0 0 110 110">
    <g transform="rotate(-90 55 55)" fill="none" stroke-width="20">
      <circle cx="55" cy="55" r="44" stroke="var(--blue)" stroke-dasharray="33.2 243.3"/>
      <circle cx="55" cy="55" r="44" stroke="var(--orange)" stroke-dasharray="58.1 218.4" stroke-dashoffset="-33.2"/>
      <circle cx="55" cy="55" r="44" stroke="var(--gray)" stroke-dasharray="165.9 110.6" stroke-dashoffset="-91.3"/>
      <circle cx="55" cy="55" r="44" stroke="var(--yellow)" stroke-dasharray="19.3 257.2" stroke-dashoffset="-257.2"/>
    </g>
    <g font-size="6" fill="#fff" text-anchor="middle">
      <text x="74" y="16">marketing</text><text x="74" y="23">12%</text>
      <text x="96" y="55">sg&amp;a</text><text x="96" y="62">21%</text>
      <text x="25" y="87">r&amp;d</text><text x="25" y="94">60%</text>
      <text x="48" y="15">1x legal</text><text x="48" y="22">7%</text>
    </g>
  </svg>
  <p class="abs body" style="left:196px;width:145px;top:72px;text-align:justify;color:#444">Lorem Ipsum is simply dummy text of the printing and typesetting industry. Lorem Ipsum has been the industry's standard dummy text ever since the 1500s, when an unknown printer took a galley of type and scrambled it to make a type specimen book. It has survived not only five centuries, but also the leap into electronic typesetting, remaining essentially unchanged. It was popularised in the 1960s with the release of Letraset sheets containing Lorem Ipsum passages, and more recently with desktop publishing software including versions of Lorem Ipsum.<br><br>It is a long established fact that a reader will be distracted by the readable content of a page when looking at its layout. The point of using Lorem Ipsum is that it has a more-or-less normal distribution of letters, as opposed to using 'Content here, content here', making it look like readable English. Many desktop publishing packages and web page editors now use Lorem Ipsum as their default model text.</p>
  <footer class="footer"><span class="bar"></span><span class="mark brand">KEYSTONE<br>LEDGER GROUP</span><span class="tab">2</span></footer>
</section>

<section class="slide c1 r3">
  <h2 class="title">BULLET TEXT</h2>
  <div class="rule"></div>
  <p class="abs body" style="left:21px;right:20px;top:38px;color:#333">Lorem Ipsum is simply dummy text of the printing and typesetting industry. Lorem Ipsum has been the industry's standard dummy text ever since the 1500s, when an unknown printer took a galley of type and scrambled it to make a type specimen book. It has survived not only five centuries, but also the leap into electronic typesetting, remaining essentially unchanged. It was popularised in the 1960s</p>
  <div class="photo" role="img" aria-label="Photo of a businessman relaxing at his desk with a laptop" style="left:30px;top:113px;width:190px;height:109px;background:linear-gradient(135deg,#eef1f4,#aeb7c2 60%,#5c6470)"></div>
  <ul class="bullets">
    <li>Lorem Ipsum is simply dummy text of the printing and typesetting industry. Lorem Ipsum has been the industry's standard dummy tex</li>
    <li>Ever since the 1500s, when an unknown printer took a galley of type and scrambled it to make a type specimen book.</li>
    <li>It has survived not only five centuries, but also the leap into electronic typesetting, remaining essentially unchanged. It was popularised in the 1960s with the release of</li>
    <li>It is a long established fact that a reader will be distracted by the readable content of a page when looking at its layout. The point of using</li>
    <li>Lorem Ipsum is that it has a more-or-less normal distribution of letters, as opposed to</li>
  </ul>
  <footer class="footer"><span class="bar"></span><span class="mark brand">KEYSTONE<br>LEDGER GROUP</span><span class="tab">3</span></footer>
</section>

<section class="slide c2 r3">
  <h2 class="title">PICTURE SLIDE</h2>
  <div class="rule"></div>
  <div class="photo" role="img" aria-label="Photo of a businessman drawing a cloud network diagram" style="left:21px;top:43px;width:166px;height:106px;background:linear-gradient(135deg,#c9d6e2,#7c8ea4 55%,#1f2c44)"></div>
  <div class="photo" role="img" aria-label="Photo of a businessman relaxing at his desk" style="left:21px;top:152px;width:83px;height:69px;background:linear-gradient(135deg,#eef0f2,#9aa3ad)"></div>
  <div class="photo" role="img" aria-label="Photo of a man in a white shirt seen from behind" style="left:106px;top:152px;width:81px;height:69px;background:linear-gradient(135deg,#e8eaec,#b8bec5)"></div>
  <svg class="abs" style="left:204px;top:43px" width="14" height="14" viewBox="0 0 14 14"><circle cx="7" cy="7" r="6" fill="#fff" stroke="#777"/><circle cx="7" cy="7" r="3.5" fill="#777"/></svg>
  <p class="abs" style="left:229px;top:45px;font-size:6.5px;font-weight:500;color:var(--blue)">Lorem ipsum dolor sit amet,</p>
  <p class="abs body" style="left:229px;width:118px;top:58px;color:#333">Lorem Ipsum is simply dummy text of the printing and typesetting industry. Lorem Ipsum has been the industry's standard dummy text ever since the 1500s, when an unknown printer took a galley of type and scrambled it to make a type specimen book. It has survived not only five centuries, but also the leap into electronic typesetting, remaining essentially unchanged. It was popularised in</p>
  <svg class="abs" style="left:204px;top:150px" width="14" height="14" viewBox="0 0 14 14"><circle cx="7" cy="7" r="6" fill="#fff" stroke="#777"/><path d="M4 10V6M7 10V4M10 10V7" stroke="#777" stroke-width="1.5"/></svg>
  <p class="abs" style="left:229px;top:152px;font-size:6.5px;font-weight:500;color:var(--blue)">Lorem ipsum dolor sit amet,</p>
  <p class="abs body" style="left:229px;width:118px;top:166px;color:#333">Lorem Ipsum is simply dummy text of the printing and typesetting industry. Lorem Ipsum has been the industry's standard dummy text ever since the 1500s, when an unknown printer took a galley of type and scrambled it to make a type specimen book. It has survived not only five centuries, but also</p>
  <footer class="footer"><span class="bar"></span><span class="mark brand">KEYSTONE<br>LEDGER GROUP</span><span class="tab">3</span></footer>
</section>

<section class="slide c3 r3">
  <h2 class="title">WHAT WE DO</h2>
  <div class="rule"></div>
  <div class="photo-circle" role="img" aria-label="Photo of a businessman at his desk" style="left:43px;background:radial-gradient(circle,#d7dbe0,#8e97a3)"></div>
  <div class="photo-circle" role="img" aria-label="Photo of a businesswoman celebrating" style="left:145px;background:radial-gradient(circle,#efe7dd,#a8927c)"></div>
  <div class="photo-circle" role="img" aria-label="Photo of a tall stack of paperwork" style="left:259px;background:radial-gradient(circle,#f2f2f2,#a9b6c4)"></div>
  <div class="card" style="left:22px"><h4>Lorem ipsum dolor sit amet, consectetur adipisic-</h4><p class="body" style="color:#444">Lorem Ipsum is simply dummy text of the printing and typesetting industry. Lorem Ipsum has been the industry's standard dummy text ever since the 1500s, when an unknown printer took a galley of type and scrambled it to make a type specimen book. It has survived not only five centuries, but also the leap into electronic typesetting, remaining essentially unchanged. It was popularised in the 1960s with the</p></div>
  <div class="card" style="left:136px"><h4>Lorem ipsum dolor sit amet, consectetur adipisic-</h4><p class="body" style="color:#444">Lorem Ipsum is simply dummy text of the printing and typesetting industry. Lorem Ipsum has been the industry's standard dummy text ever since the 1500s, when an unknown printer took a galley of type and scrambled it to make a type specimen book. It has survived not only five centuries, but also the leap into electronic typesetting, remaining essentially unchanged. It was</p></div>
  <div class="card" style="left:250px"><h4>Lorem ipsum dolor sit amet, consectetur adipisic-</h4><p class="body" style="color:#444">Lorem Ipsum is simply dummy text of the printing and typesetting industry. Lorem Ipsum has been the industry's standard dummy text ever since the 1500s, when an unknown printer took a galley of type and scrambled it to make a type specimen book. It has survived not only five centuries, but also the leap into electronic typesetting, remaining essentially unchanged. It was</p></div>
  <footer class="footer"><span class="bar"></span><span class="mark brand">KEYSTONE<br>LEDGER GROUP</span><span class="tab">3</span></footer>
</section>

<section class="slide light c1 r4">
  <div class="side-art on-white-soft" role="img" aria-label="Soft decorative geometric panel in pale blue tones"></div>
  <div class="contact">
    <span class="brand" style="color:var(--navy)">KEYSTONE<br>LEDGER GROUP</span>
    <div>P: +00 100 200 3000<br>F: +00 100 200 3001</div>
    <div>hello@keystoneledger.example<br>www.keystoneledger.example</div>
    <div>P.O. Box 0000, Sample<br>City 00000, xxx</div>
  </div>
</section>

<section class="slide dark c2 r4">
  <div class="side-art on-navy" role="img" aria-label="Faint decorative geometric panel"></div>
  <div class="contact">
    <span class="brand" style="color:#fff">KEYSTONE<br>LEDGER GROUP</span>
    <div>P: +00 100 200 3000<br>F: +00 100 200 3001</div>
    <div>hello@keystoneledger.example<br>www.keystoneledger.example</div>
    <div>P.O. Box 0000, Sample<br>City 00000, xxx</div>
  </div>
</section>

</main>
</body>
</html>
```